Independence Day Graphics for Sale

I want to create 10 social media graphics (new Pictora size 4:5 (1080 x 1350 pixels) focusing on our July 4th Sale Graphics, using any of the pics attached. Use the attached pics, NO RANDOM STOCK PHOTOGRAPHY. For the color scheme of the graphics, they should all be complementary to the product colors in the photos.
You can add any of the photos attached but none are required. You can do some of the graphics in all text. I mainly need BOLD text that says one of the headlines (10 total) SEE ATTACHED WORD DOCUMENT for the headlines to use.

Target Market(s)

women looking to lose weight

Requirements
Must have
• pics attached and text attached

```html
<!DOCTYPE html>
<html lang="en">
<head>
<meta charset="UTF-8">
<title>25% Off Stock Up Event</title>
<link rel="stylesheet" href="https://fonts.googleapis.com/css2?family=Poppins:wght@700;800&display=swap">
<style>
  :root {
    --sale-red: #ea2e2e;
    --badge-black: #1e1e1f;
    --paper: #ffffff;
    --photo-light: #f4efec;
    --photo-mid: #d9c2b4;
    --photo-dark: #2a2324;
  }
  * { margin: 0; padding: 0; box-sizing: border-box; }
  html, body { width: 960px; height: 1200px; overflow: hidden; background: var(--paper); }
  .poster {
    position: relative;
    width: 960px;
    height: 1200px;
    overflow: hidden;
    background: var(--paper);
    font-family: "Poppins", Arial, sans-serif;
    font-weight: 800;
    line-height: 1;
  }
  .headline-line {
    position: absolute;
    right: 31px;
    font-size: 200px;
    letter-spacing: -4px;
    color: var(--sale-red);
    white-space: nowrap;
  }
  .headline-line--one { top: 8px; }
  .headline-line--two { top: 167px; }
  .headline-line--three { top: 320px; }

  .model-photo {
    position: absolute;
    left: 0;
    top: 505px;
    width: 505px;
    height: 695px;
    background: linear-gradient(180deg, var(--photo-dark) 0%, var(--photo-mid) 30%, var(--photo-light) 55%, var(--photo-light) 85%, var(--photo-dark) 100%);
    border-radius: 240px 240px 0 0;
  }

  .offer-badge {
    position: absolute;
    left: 505px;
    top: 529px;
    width: 393px;
    height: 392px;
    border-radius: 60px;
    background: var(--badge-black);
    box-shadow: 12px 14px 26px rgba(0, 0, 0, 0.35);
  }
  .badge-text {
    position: absolute;
    color: var(--paper);
    white-space: nowrap;
    letter-spacing: -3px;
  }
  .badge-text--percent { left: 550px; top: 571px; font-size: 163px; }
  .badge-text--off { left: 541px; top: 695px; font-size: 177px; }

  .scope-all {
    position: absolute;
    left: 526px;
    top: 834px;
    font-size: 208px;
    letter-spacing: -6px;
    color: var(--sale-red);
    text-shadow: 6px 8px 14px rgba(0, 0, 0, 0.3);
    white-space: nowrap;
  }
  .scope-products {
    position: absolute;
    right: 30px;
    top: 1024px;
    font-size: 80px;
    font-weight: 700;
    letter-spacing: -1px;
    color: var(--sale-red);
    white-space: nowrap;
  }
</style>
</head>
<body>
  <main class="poster">
    <h1 class="headline">
      <span class="headline-line headline-line--one">25% OFF</span>
      <span class="headline-line headline-line--two">STOCK</span>
      <span class="headline-line headline-line--three">UP EVENT</span>
    </h1>

    <div class="model-photo" role="img" aria-label="Smiling woman with long dark hair in a white cropped sweater holding a bottle of Core Bloom supplements"></div>

    <div class="offer-badge" aria-hidden="true"></div>
    <p class="badge-text badge-text--percent">25%</p>
    <p class="badge-text badge-text--off">OFF</p>

    <p class="scope-all">ALL</p>
    <p class="scope-products">SUPPLEMENTS</p>
  </main>
</body>
</html>
```